Business Card for Wellness Clinic

We need a business card for our new logo. I want it to match the feel of the logo

Target Market(s)

Young professional families looking for holistic health care

Industry/Entity Type

Health And Wellness

Contact Information for Business Card

Our business Name: Brackenfield Health & wellness Centre, our phone #, email address...see attached old business card

Font styles to use
Sans Serif

Colors
33b8a4
cee9f5

Requirements
Must have
• my logo and business name
• Font is "Helvetica Neue LT Std 45 Light" and
• Only for "&" using font "Trajan pro bold"
• Use colors in the logo

```html
<!DOCTYPE html>
<html lang="en">
<head>
<meta charset="utf-8">
<title>Brackenfield Health &amp; Wellness Centre – Business Cards</title>
<link rel="stylesheet" href="https://fonts.googleapis.com/css2?family=Cinzel:wght@600&family=Roboto:wght@300;400&display=swap">
<style>
  :root {
    --teal: #33b8a4;
    --teal-deep: #1fae98;
    --sky: #cee9f5;
    --sky-icon: #a9d8ee;
    --ink: #4a4a4a;
    --paper: #ffffff;
    --stage: #eef2f3;
  }
  * { box-sizing: border-box; margin: 0; padding: 0; }
  html, body {
    width: 1200px; height: 1200px; overflow: hidden;
    background: var(--stage);
    font-family: "Roboto", "Helvetica Neue", Arial, sans-serif;
    font-weight: 300;
  }
  .sheet {
    width: 1200px; height: 1200px;
    display: flex; flex-direction: column; align-items: center; justify-content: center;
    gap: 50px;
  }
  .card {
    position: relative;
    width: 880px; height: 503px;
    background: var(--paper);
    border-radius: 30px;
    overflow: hidden;
    box-shadow: 0 6px 18px rgba(0,0,0,0.12);
  }
  .brand {
    position: absolute; left: 48px; top: 58px;
    display: flex; align-items: center; gap: 26px;
  }
  .brand-mark {
    width: 92px; height: 92px; border-radius: 14px;
    background: var(--teal);
    flex: none;
  }
  .brand-name {
    font-family: "Cinzel", "Trajan Pro", serif;
    font-weight: 600;
    color: var(--teal);
    font-size: 44px;
    line-height: 1.02;
    letter-spacing: 1px;
  }

  /* Appointment card */
  .appointment .rule {
    position: absolute; left: 0; right: 0; top: 212px; height: 5px;
    background: var(--teal);
  }
  .appointment .band {
    position: absolute; left: 0; right: 0; top: 232px; bottom: 0;
    background: var(--teal);
    color: var(--paper);
    padding: 36px 48px 0;
  }
  .fields {
    display: grid; grid-template-columns: 1fr 1fr; column-gap: 40px; row-gap: 30px;
    font-size: 22px;
  }
  .field { display: flex; align-items: flex-end; gap: 12px; }
  .field .line { flex: 1; border-bottom: 1.5px solid var(--paper); height: 22px; }
  .field.wide { grid-column: 2; grid-row: 1 / span 2; flex-direction: column; align-items: stretch; gap: 30px; }
  .field.wide .row { display: flex; align-items: flex-end; gap: 12px; }
  .notice {
    margin-top: 38px;
    border-top: 2px dashed var(--paper);
    padding-top: 16px;
    font-size: 15.5px;
    letter-spacing: 0.2px;
  }

  /* Contact card */
  .contact .nameplate {
    position: absolute; left: 0; top: 300px;
    width: 440px; height: 96px;
    background: var(--teal);
    border-radius: 0 48px 48px 0;
    color: var(--paper);
    display: flex; align-items: center; gap: 18px;
    padding-left: 28px;
  }
  .nameplate-square { width: 34px; height: 34px; border: 2px solid var(--paper); border-radius: 6px; flex: none; }
  .person-name { font-size: 27px; font-weight: 400; line-height: 1.1; }
  .person-role { font-size: 19px; }
  .details {
    position: absolute; right: 48px; top: 200px;
    width: 380px;
    display: flex; flex-direction: column; gap: 26px;
    color: var(--ink); font-size: 20px; line-height: 1.3;
  }
  .detail { display: flex; align-items: flex-start; gap: 14px; }
  .detail svg { width: 34px; height: 34px; flex: none; }
  .web {
    position: absolute; left: 48px; bottom: 44px;
    display: flex; align-items: center; gap: 14px;
    color: var(--ink); font-size: 20px;
  }
  .web svg { width: 30px; height: 30px; }
</style>
</head>
<body>
<main class="sheet">

  <section class="card appointment" aria-label="Appointment card">
    <div class="brand">
      <span class="brand-mark" aria-hidden="true"></span>
      <h1 class="brand-name">Brackenfield Health &amp;<br>Wellness Centre</h1>
    </div>
    <div class="rule"></div>
    <div class="band">
      <div class="fields">
        <div class="field"><span>Date :</span><span class="line"></span></div>
        <div class="field wide">
          <div class="row"><span>For :</span><span class="line"></span></div>
          <div class="row"><span class="line"></span></div>
        </div>
        <div class="field"><span>Time :</span><span class="line"></span></div>
      </div>
      <p class="notice">If you are unable to keep your appointment, please provide at least 2 business day notice or full visit fees will apply.</p>
    </div>
  </section>

  <section class="card contact" aria-label="Contact card">
    <div class="brand">
      <span class="brand-mark" aria-hidden="true"></span>
      <h2 class="brand-name">Brackenfield Health &amp;<br>Wellness Centre</h2>
    </div>

    <div class="nameplate">
      <span class="nameplate-square" aria-hidden="true"></span>
      <div>
        <p class="person-name">Dr. Maren Holloway, N.D.</p>
        <p class="person-role">Naturopathic Doctor.</p>
      </div>
    </div>

    <div class="details">
      <div class="detail">
        <svg viewBox="0 0 34 34" aria-hidden="true">
          <circle cx="17" cy="17" r="17" fill="var(--sky-icon)"/>
          <path d="M17 8a6 6 0 0 0-6 6c0 5 6 11 6 11s6-6 6-11a6 6 0 0 0-6-6z" fill="none" stroke="#fff" stroke-width="2"/>
          <circle cx="17" cy="14" r="2" fill="#fff"/>
        </svg>
        <p>48 Larchmont Ave, Suite 210<br>Kingsford, ON K9X 2B7<br>555-014-2273</p>
      </div>
      <div class="detail">
        <svg viewBox="0 0 34 34" aria-hidden="true">
          <circle cx="17" cy="17" r="17" fill="var(--sky-icon)"/>
          <rect x="9" y="11" width="16" height="12" rx="1.5" fill="none" stroke="#fff" stroke-width="2"/>
          <path d="M9 12l8 6 8-6" fill="none" stroke="#fff" stroke-width="2"/>
        </svg>
        <p>mholloway@brackenfieldwellness.ca</p>
      </div>
    </div>

    <div class="web">
      <svg viewBox="0 0 30 30" aria-hidden="true">
        <circle cx="15" cy="15" r="15" fill="var(--sky-icon)"/>
        <circle cx="15" cy="15" r="8" fill="none" stroke="#fff" stroke-width="1.6"/>
        <ellipse cx="15" cy="15" rx="3.5" ry="8" fill="none" stroke="#fff" stroke-width="1.6"/>
        <path d="M7 15h16" stroke="#fff" stroke-width="1.6"/>
      </svg>
      <span>www.brackenfieldwellness.ca</span>
    </div>
  </section>

</main>
</body>
</html>
```